Beauty Page

**UPDATED Brief**
We are looking for a website for a beauty organisation that targets both MEN & WOMAN. The focus of the company is in four main areas:

- Health
* Naturopathy & Remedial Massage
- Body
* Yoga
* Personal Training
* Massage
- Skin
* Skin care products such as Velmoracine
- Beauty
* Waxing
* Eye Treatments

We have attached the logo, (a sample of the website that I did - based on the book) and the sample of the pdf book
Updates

Dear All,

Thank you for your patience regarding the beauty contest. We were not happy with the designs that were submitted to us. We therefore had the Graphic designer to do the pricelist book to get all the colours for the organisation.

We are now happy to relaunch the contest and invite you all to take a look at the brief, download a sample of the book and the website we designed on what I’m looking for (the website is only a draft so I don’t want you to copy it) and let your creative mind go wild and present some suggestions to us.

Thanks

 

Target Market(s)

Woman & Men age 24 - 60

Industry/Entity Type

It Company

Requirements
Must have
• Use of main colours
Black
White
Gray - (CYMK - 65, 58, 57, 37)
Purpleish - Maroon (CYMK - 52, 69, 47, 25)

Use of the three color dots on the page.
(white, maroon & Gray)
Same fonts as the book
- Helvetica LT Std
Should not have
• Logo must not be altered i.e different colours, fonts, shadows etc...

```html
<!DOCTYPE html>
<html lang="en">
<head>
<meta charset="utf-8">
<title>Bodyline &amp; Beauty</title>
<link href="https://fonts.googleapis.com/css2?family=PT+Sans+Narrow:wght@400;700&family=Roboto:wght@400;500&display=swap" rel="stylesheet">
<style>
:root{
  --maroon:#6a0c3c;
  --maroon-dark:#520830;
  --maroon-light:#8c2a5f;
  --rose:#9b2d66;
  --grey:#7a7a7a;
  --grey-dark:#4a4a4a;
  --line:#dcdcdc;
  --panel:#f6f6f6;
  --white:#ffffff;
  --lime:#b5c92a;
}
*{box-sizing:border-box;margin:0;padding:0}
html,body{width:993px;height:1200px;overflow:hidden;background:var(--white)}
body{position:relative;font-family:"Roboto",Arial,sans-serif;color:var(--grey-dark)}
.abs{position:absolute}
.page-frame{left:17px;top:17px;width:954px;height:1165px;border:1px solid var(--line)}
.contact-tab{left:697px;top:19px;width:221px;height:28px;background:var(--white);border:1px solid var(--line);border-top:none;box-shadow:0 2px 3px rgba(0,0,0,.1);font:700 15px "PT Sans Narrow",Arial,sans-serif;color:var(--maroon-dark);display:flex;align-items:center}
.contact-tab span{padding-left:50px;flex:1}
.contact-tab .toggle{width:40px;height:100%;border-left:1px solid var(--line);display:flex;align-items:center;justify-content:center}
.header{left:68px;top:63px;width:855px;height:92px;background:linear-gradient(#fafafa,#ececec);box-shadow:0 2px 5px rgba(0,0,0,.15)}
.brand{left:88px;top:92px;font:700 30px "PT Sans Narrow",Arial,sans-serif;color:var(--maroon);letter-spacing:.5px}
.join{left:832px;top:74px;width:71px;height:72px;border-radius:9px;background:linear-gradient(#d84a92,#8c1d55);border:2px solid #c23a7d;color:var(--white);text-align:center;font:700 19px/18px "PT Sans Narrow",Arial,sans-serif;padding-top:7px}
.join small{display:block;font-size:8px;line-height:8px;margin-top:3px}
.nav{left:68px;top:156px;width:855px;height:33px;background:linear-gradient(#8a2860,var(--maroon-dark));display:flex;justify-content:flex-end}
.nav a{color:var(--white);text-decoration:none;font:700 15px/33px "PT Sans Narrow",Arial,sans-serif;padding:0 17px;border-left:1px solid rgba(255,255,255,.18)}
.nav a:first-child{border-left:none}
.hero{left:73px;top:196px;width:849px;height:271px;border:1px solid var(--line);background:var(--white);overflow:hidden;box-shadow:0 8px 8px -6px rgba(0,0,0,.35)}
.hero h1{position:absolute;left:58px;top:40px;font:700 44px/45px "PT Sans Narrow",Arial,sans-serif;color:var(--rose)}
.hero h1 b{color:var(--maroon-dark)}
.hero p{position:absolute;left:58px;top:142px;width:380px;font:19px/23px "PT Sans Narrow",Arial,sans-serif;color:var(--rose)}
.hero .btn{position:absolute;left:59px;top:204px;width:105px;height:31px;background:var(--maroon);color:var(--white);font:18px/31px "PT Sans Narrow",Arial,sans-serif;text-align:center}
.hero-photo{position:absolute;left:538px;top:0;width:311px;height:271px;background:radial-gradient(ellipse at 55% 55%,#f2d2c0 0%,#f6e6dc 45%,#ffffff 80%)}
.arrow{width:16px;height:32px;background:var(--maroon);display:flex;align-items:center;justify-content:center}
.welcome{left:0;top:514px;width:993px;text-align:center;font:700 41px "PT Sans Narrow",Arial,sans-serif;color:var(--maroon)}
.intro{left:125px;top:567px;width:743px;text-align:center;font:19px/27px "PT Sans Narrow",Arial,sans-serif;color:var(--grey)}
.card{top:651px;width:271px;height:180px;border:1px solid var(--line);background:var(--white);box-shadow:0 8px 8px -6px rgba(0,0,0,.25)}
.card .bar{position:absolute;left:-1px;right:-1px;bottom:-1px;height:38px;background:linear-gradient(#7e1f55,var(--maroon-dark));color:var(--white);font:700 19px/38px "PT Sans Narrow",Arial,sans-serif;padding-left:27px}
.card .bar svg{position:absolute;right:14px;top:11px}
.badge-shape{position:absolute;left:14px;top:54px;width:240px;height:40px;background:linear-gradient(90deg,#e9eef4,#f5f5f5);border-radius:4px}
.stones-photo{position:absolute;left:60px;top:10px;width:150px;height:120px;background:linear-gradient(#eef3e4,#d8d8d8)}
.ribbon{position:absolute;left:0;top:0}
.repair{position:absolute;right:10px;top:10px;text-align:right;font:19px/20px "PT Sans Narrow",Arial,sans-serif;color:var(--rose)}
.repair b{color:var(--maroon-dark);font-size:21px}
.partner-name{position:absolute;left:0;width:100%;top:68px;text-align:center;font:700 28px "PT Sans Narrow",Arial,sans-serif;color:#2e2c8a}
.rule{left:76px;top:857px;width:848px;height:1px;background:#ececec}
.offers-title{left:85px;top:876px;font:700 20px "PT Sans Narrow",Arial,sans-serif;color:var(--maroon-dark)}
.offer{left:75px;width:276px;border:1px solid var(--line);background:linear-gradient(#fff,#f3f3f3);box-shadow:0 2px 3px rgba(0,0,0,.12);padding:8px 12px 0 32px}
.offer h3{font:18px "PT Sans Narrow",Arial,sans-serif;color:var(--grey-dark);font-weight:400}
.offer h3 span{color:var(--rose);font-family:"Roboto",Arial,sans-serif;font-size:12px}
.offer p{font-size:13px;line-height:17px;color:var(--grey-dark);margin-top:4px}
.offer svg{position:absolute;left:12px;top:14px}
.promo{left:376px;top:889px;width:545px;height:198px;border:1px solid #eee;background:var(--white);box-shadow:0 8px 8px -6px rgba(0,0,0,.35)}
.promo h2{position:absolute;left:28px;top:22px;font:400 40px Arial,sans-serif;color:var(--lime)}
.promo p{position:absolute;left:35px;top:73px;width:306px;text-align:center;font:19px/23px "PT Sans Narrow",Arial,sans-serif;color:var(--grey)}
.product-shot{position:absolute;left:360px;top:26px;width:154px;height:142px;background:linear-gradient(#ededed,#cfcfcf);border-radius:3px}
.footer-rule{left:76px;top:1114px;width:848px;height:1px;background:#ececec}
.connect{left:77px;top:1131px;font:700 19px "PT Sans Narrow",Arial,sans-serif;color:var(--maroon)}
.social{top:1130px;width:28px;height:28px;border-radius:50%;background:linear-gradient(#ffffff,#e2e2e2);border:1px solid #d4d4d4}
.legal{left:730px;top:1134px;font-size:12px;color:var(--grey-dark);display:flex;gap:12px}
.legal span+span{border-left:1px solid var(--line);padding-left:12px}
</style>
</head>
<body>
<div class="abs page-frame"></div>

<div class="abs contact-tab"><span>CONTACT US TODAY!</span><div class="toggle"><svg width="12" height="8"><path d="M1 1l5 5 5-5" fill="none" stroke="#6a0c3c" stroke-width="2"/></svg></div></div>

<header class="abs header"></header>
<div class="abs brand">BODYLINE &amp; BEAUTY</div>
<div class="abs join">JOIN<br>TODAY<small>FOR DISCOUNTS<br>AND OFFERS</small></div>

<nav class="abs nav"><a>HOME</a><a>ABOUT US</a><a>SERVICES &amp; TREATMENT</a><a>CONTACT US</a></nav>

<section class="abs hero">
  <h1>HELPING YOU TO <b>LOVE</b> YOUR<br>SKIN AND <b>FEEL GOOD</b></h1>
  <p>Through our treatments, products and education we aim to give you total body wellbeing.</p>
  <div class="btn">Find our more</div>
  <div class="hero-photo" role="img" aria-label="Photo of a relaxed spa client in a white towel holding a white lily"></div>
</section>
<div class="abs arrow" style="left:74px;top:315px"><svg width="8" height="12"><path d="M7 1L2 6l5 5" fill="none" stroke="#fff" stroke-width="2"/></svg></div>
<div class="abs arrow" style="left:906px;top:315px"><svg width="8" height="12"><path d="M1 1l5 5-5 5" fill="none" stroke="#fff" stroke-width="2"/></svg></div>

<h2 class="abs welcome">WELCOME TO BODYLINE &amp; BEAUTY</h2>
<p class="abs intro">We are a family established health, massage, skincare centre that provides quality professional treatments and education to each and every client. We pride ourslеves on being able to cater for all individuals.</p>

<div class="abs card" style="left:76px">
  <div class="badge-shape" role="img" aria-label="Silverleaf Guild partner badge"></div>
  <div class="bar">ABOUT US<svg width="10" height="16"><path d="M2 2l6 6-6 6" fill="none" stroke="#fff" stroke-width="3"/></svg></div>
</div>
<div class="abs card" style="left:364px">
  <div class="stones-photo" role="img" aria-label="Photo of stacked black massage stones topped with a green leaf"></div>
  <div class="bar">SERVICES &amp; TREATMENTS<svg width="10" height="16"><path d="M2 2l6 6-6 6" fill="none" stroke="#fff" stroke-width="3"/></svg></div>
</div>
<div class="abs card" style="left:654px">
  <svg class="ribbon" width="80" height="80"><path d="M0 0h80L0 80z" fill="#cfe3f0"/><text x="8" y="48" transform="rotate(-45 22 40)" font-family="PT Sans Narrow,Arial,sans-serif" font-weight="700" font-size="17" fill="#fff">NEW</text></svg>
  <div class="repair"><b>Correct and repair</b><br>skin range available now!</div>
  <div class="partner-name">MARÉ LUMIÈRE</div>
  <div class="bar">PRODUCT RANGES<svg width="10" height="16"><path d="M2 2l6 6-6 6" fill="none" stroke="#fff" stroke-width="3"/></svg></div>
</div>

<div class="abs rule"></div>
<h2 class="abs offers-title">LATEST OFFERS</h2>
<div class="abs offer" style="top:910px;height:77px"><svg width="10" height="8"><path d="M1 1l4 4 4-4" fill="none" stroke="#6a0c3c" stroke-width="2"/></svg><h3>CURRENT OFFER <span>- Ends 21st of June</span></h3><p>Eu vim fugit eligendi salutatus, nominati quaestio an usu.</p></div>
<div class="abs offer" style="top:998px;height:37px"><svg width="8" height="10"><path d="M1 1l4 4-4 4" fill="none" stroke="#6a0c3c" stroke-width="2"/></svg><h3>CURRENT OFFER <span>- Ends 21st of June</span></h3></div>
<div class="abs offer" style="top:1045px;height:37px"><svg width="8" height="10"><path d="M1 1l4 4-4 4" fill="none" stroke="#6a0c3c" stroke-width="2"/></svg><h3>CURRENT OFFER <span>- Ends 21st of June</span></h3></div>

<section class="abs promo">
  <h2>ClearPhase Care</h2>
  <p>A 24 - hour treatment system that uses the state-of-the-art technology to tackle adult breakouts. Each product is designed to be layered for maximum effectiveness.</p>
  <div class="product-shot" role="img" aria-label="Product photo of the Velmoracine clearing range bottles and tubes"></div>
</section>
<div class="abs arrow" style="left:377px;top:975px"><svg width="8" height="12"><path d="M7 1L2 6l5 5" fill="none" stroke="#fff" stroke-width="2"/></svg></div>
<div class="abs arrow" style="left:905px;top:975px"><svg width="8" height="12"><path d="M1 1l5 5-5 5" fill="none" stroke="#fff" stroke-width="2"/></svg></div>

<div class="abs footer-rule"></div>
<div class="abs connect">CONNECT WITH US!</div>
<div class="abs social" style="left:221px" role="img" aria-label="Social link one"></div>
<div class="abs social" style="left:257px" role="img" aria-label="Social link two"></div>
<div class="abs social" style="left:294px" role="img" aria-label="News feed"></div>
<div class="abs legal"><span>Privacy Policy</span><span>Terms of use</span></div>
</body>
</html>
```